Company letter head

Hello,
We are a global logistics company requiring a letterhead design for all our company documentation.
Company Name: Clearly display the full name of your company at the top of the letterhead.
Logo: Include your company logo for brand recognition.
Contact Information: This includes your company's address, phone number, email address, and website URL.
Target Market(s)
Clients/customers
Industry/Entity Type
Logistics
Font styles to use
Sans Serif
Requirements
Must have
- Company name and logo
Nice to have
- borders, header/footers

```html
<!DOCTYPE html>
<html lang="en">
<head>
<meta charset="utf-8">
<title>Northline Freight – Letterhead and Envelope</title>
<link rel="stylesheet" href="https://fonts.googleapis.com/css2?family=Open+Sans:wght@400;600;700;800&display=swap">
<style>
  :root {
    --bg: #e8e8e8;
    --paper: #f7f7f7;
    --red: #c52a32;
    --charcoal: #3e3e3e;
    --ink: #4a4a4a;
    --rule: #5a5a5a;
    --sign-fill: #e4e6ea;
    --white: #ffffff;
  }
  * { box-sizing: border-box; margin: 0; padding: 0; }
  html, body {
    width: 1200px; height: 795px; overflow: hidden;
    background: var(--bg);
    font-family: "Open Sans", Arial, sans-serif;
  }
  .canvas { position: relative; width: 1200px; height: 795px; }

  /* Letterhead sheet */
  .letterhead {
    position: absolute; left: 70px; top: 30px;
    width: 520px; height: 735px;
    background: var(--paper);
    box-shadow: 0 2px 10px rgba(0,0,0,.12);
    overflow: hidden;
  }
  .letterhead__brand {
    position: absolute; left: 50px; top: 54px;
    display: flex; align-items: center; gap: 10px;
  }
  .brand-mark { width: 34px; height: 34px; border-radius: 50%; background: var(--charcoal); flex: none; }
  .brand-name {
    font-weight: 800; font-size: 21px; line-height: 1;
    color: var(--red); text-transform: uppercase; letter-spacing: .3px;
  }
  .letterhead__contact {
    position: absolute; right: 40px; top: 52px;
    font-style: normal;
    font-size: 8.5px; line-height: 13px; color: var(--ink);
  }
  .contact-company { font-weight: 600; font-size: 9.5px; margin-bottom: 2px; color: #333; }
  .contact-row { display: flex; align-items: center; gap: 5px; }
  .contact-row svg { width: 8px; height: 8px; flex: none; }
  .letterhead__rule {
    position: absolute; left: 46px; right: 40px; top: 112px;
    height: 1px; background: var(--rule);
  }
  .letterhead__body {
    position: absolute; left: 52px; right: 48px; top: 150px;
    font-size: 8.4px; line-height: 14px; color: var(--ink);
  }
  .salutation { margin-bottom: 8px; }
  .letterhead__body p.para { text-indent: 18px; margin-bottom: 12px; }
  .closing { margin-top: 4px; }
  .signature {
    position: absolute; left: 58px; top: 512px;
    width: 70px; height: 40px;
  }
  .letterhead__footer { position: absolute; left: 0; bottom: 0; width: 520px; height: 22px; }

  /* Envelope */
  .envelope {
    position: absolute; left: 625px; top: 250px;
    width: 545px; height: 290px;
    background: var(--paper);
    box-shadow: 0 2px 10px rgba(0,0,0,.12);
  }
  .envelope__flap {
    position: absolute; left: 0; top: 0; right: 0; height: 112px;
    background: var(--red);
    border-radius: 0 0 18px 18px;
  }
  .envelope__brand {
    position: absolute; left: 300px; top: 40px;
    display: flex; align-items: center; gap: 8px;
  }
  .envelope__brand .brand-mark { background: var(--white); width: 28px; height: 28px; }
  .envelope__brand .brand-name { color: var(--white); font-size: 17px; }
</style>
</head>
<body>
<main class="canvas">

  <section class="letterhead" aria-label="Company letterhead">
    <div class="letterhead__brand">
      <span class="brand-mark"></span>
      <span class="brand-name">Northline Freight</span>
    </div>

    <address class="letterhead__contact">
      <div class="contact-company">Northline Freight</div>
      <div class="contact-row">
        <svg viewBox="0 0 10 10" aria-hidden="true"><path d="M2 1l2 2-1 1.5c.6 1.2 1.4 2 2.5 2.5L7 6l2 2-1.2 1.4C4.5 9 1 5.5.6 2.2z" fill="var(--red)"/></svg>
        <span>(555)210-0148</span>
      </div>
      <div class="contact-row">
        <svg viewBox="0 0 10 10" aria-hidden="true"><rect x="0.5" y="2" width="9" height="6" fill="none" stroke="var(--red)" stroke-width="1.2"/><path d="M.5 2l4.5 3.5L9.5 2" fill="none" stroke="var(--red)" stroke-width="1.2"/></svg>
        <span>hello@northlinefreight.com</span>
      </div>
      <div class="contact-row">
        <svg viewBox="0 0 10 10" aria-hidden="true"><circle cx="5" cy="5" r="4.2" fill="none" stroke="var(--red)" stroke-width="1.1"/><path d="M1 5h8M5 .8c-2 2.5-2 5.9 0 8.4M5 .8c2 2.5 2 5.9 0 8.4" fill="none" stroke="var(--red)" stroke-width=".8"/></svg>
        <span>www.northlinefreight.com</span>
      </div>
    </address>

    <div class="letterhead__rule"></div>

    <div class="letterhead__body">
      <p class="salutation">Dear customer,</p>
      <p class="para">Lorem ipsum dolor sit amet, consectetur adipisicing elit, sed do eiusmod tempor incididunt ut labore et dolore magna aliqua. Ut enim ad minim veniam, quis nostrud exercitation ullamco laboris nisi ut aliquip ex ea commodo consequat. Duis aute irure dolor in reprehenderit in voluptate velit esse cillum dolore eu fugiat nulla pariatur. Excepteur sint occaecat cupidatat non proident, sunt in culpa qui officia deserunt mollit anim id est laborum.</p>
      <p class="para">Lorem ipsum dolor sit amet, consectetur adipisicing elit, sed do eiusmod tempor incididunt ut labore et dolore magna aliqua. Ut enim ad minim veniam, quis nostrud exercitation ullamco laboris nisi ut aliquip ex ea commodo consequat. Duis aute irure dolor in reprehenderit in voluptate velit esse cillum dolore eu fugiat nulla pariatur. Excepteur sint occaecat cupidatat non proident, sunt in culpa qui officia deserunt mollit anim id est laborum.</p>
      <p class="para">Lorem ipsum dolor sit amet, consectetur adipisicing elit, sed do eiusmod tempor incididunt ut labore et dolore magna aliqua. Ut enim ad minim veniam, quis nostrud exercitation ullamco laboris nisi ut aliquip ex ea commodo consequat. Duis aute irure dolor in reprehenderit in voluptate velit esse cillum dolore eu fugiat nulla pariatur. Excepteur sint occaecat cupidatat non proident, sunt in culpa qui officia deserunt mollit anim id est laborum.</p>
      <p class="para">Lorem ipsum dolor sit amet, consectetur adipisicing elit, sed do eiusmod tempor incididunt ut labore et dolore magna aliqua. Ut enim ad minim veniam, quis nostrud exercitation ullamco laboris nisi ut aliquip ex ea commodo consequat. Duis aute irure dolor in reprehenderit.</p>
      <p class="closing">Yours Sincerely,</p>
    </div>

    <svg class="signature" role="img" aria-label="Handwritten signature" viewBox="0 0 70 40">
      <rect x="0" y="8" width="70" height="26" rx="4" fill="var(--sign-fill)"/>
    </svg>

    <svg class="letterhead__footer" viewBox="0 0 520 22" preserveAspectRatio="none" aria-hidden="true">
      <rect x="0" y="15" width="370" height="7" fill="var(--red)"/>
      <polygon points="362,22 378,4 520,4 520,22" fill="var(--charcoal)"/>
    </svg>
  </section>

  <section class="envelope" aria-label="Company envelope">
    <div class="envelope__flap"></div>
    <div class="envelope__brand">
      <span class="brand-mark"></span>
      <span class="brand-name">Northline Freight</span>
    </div>
  </section>

</main>
</body>
</html>
```